Norvale Rentals and Supply Flyer

A4 flyer to send electronic to potential customer via email to tell them about Norvale Rentals.
We are start up company looking at sending companies a flyer to introduce the business.

No Folds required - just a standard A4 design

Target Market(s)

Concrete and construction companies

Industry/Entity Type

Construction Company

Font styles to use
Sans Serif

Colors
fbee3e

Requirements
Must have
• Norvale Logo
• Images provided
Nice to have
• Black and Yellow colour scheme
Should not have
• n/a

```html
<!DOCTYPE html>
<html lang="en">
<head>
<meta charset="utf-8">
<title>Norvale Rentals and Supply Flyer</title>
<link rel="stylesheet" href="https://fonts.googleapis.com/css2?family=Alfa+Slab+One&family=Catamaran:wght@800&family=Roboto+Condensed:wght@700&family=Raleway:wght@400;600&display=swap">
<style>
  :root {
    --yellow: #fbe04a;
    --brand-yellow: #fbee3e;
    --black: #0b0b0b;
    --white: #ffffff;
    --panel: rgba(0, 0, 0, 0.78);
    --photo-dark: #3a3836;
    --photo-mid: #57534f;
  }
  * { margin: 0; padding: 0; box-sizing: border-box; }
  html, body { width: 848px; height: 1200px; overflow: hidden; background: #222; }
  .flyer {
    position: relative; width: 848px; height: 1200px; overflow: hidden;
    font-family: "Raleway", sans-serif; color: var(--white);
  }
  .backdrop {
    position: absolute; inset: 0;
    background: radial-gradient(ellipse at 60% 40%, var(--photo-mid), var(--photo-dark) 70%, #2a2827);
  }
  .corner { position: absolute; inset: 0; width: 848px; height: 1200px; }
  .logo-block {
    position: absolute; left: 38px; top: 12px; width: 344px; height: 116px;
    background: var(--black); display: flex; align-items: center; justify-content: center; gap: 12px;
  }
  .logo-mark { width: 22px; height: 22px; background: var(--yellow); }
  .logo-name {
    font-family: "Catamaran", sans-serif; font-weight: 800; font-size: 36px;
    color: var(--yellow); letter-spacing: 1px;
  }
  .headline {
    position: absolute; left: 34px; top: 140px;
    font-family: "Alfa Slab One", sans-serif; color: var(--yellow);
    font-size: 72px; line-height: 88px; font-weight: 400;
  }
  .subhead {
    position: absolute; left: 28px; top: 348px;
    font-family: "Catamaran", sans-serif; font-weight: 800; font-size: 35px;
    line-height: 45px; letter-spacing: 1px; text-transform: uppercase;
  }
  .services {
    position: absolute; left: 28px; top: 440px; width: 696px; height: 296px;
    background: var(--panel); padding: 12px 14px 0 10px; list-style: none;
  }
  .services li {
    position: relative; padding-left: 22px; color: var(--yellow);
    font-size: 26px; line-height: 29.5px; letter-spacing: 3.2px;
  }
  .services li::before { content: "•"; position: absolute; left: 2px; }
  .accent-bar { position: absolute; left: 52px; top: 746px; width: 138px; height: 16px; background: var(--yellow); }
  .promise {
    position: absolute; left: 52px; top: 768px;
    font-family: "Roboto Condensed", sans-serif; font-weight: 700; font-size: 24px;
    letter-spacing: 0.6px; text-transform: uppercase;
  }
  .product { position: absolute; top: 804px; height: 218px; }
  .product-saw { left: 52px; width: 234px; background: linear-gradient(135deg, #f1f1f1, #e08a3c 60%, #c9c9c9); }
  .product-grinder { left: 292px; width: 234px; background: linear-gradient(160deg, #b82a2a, #2b2b2b 65%, #555); }
  .product-vacuum { left: 532px; width: 234px; background: linear-gradient(150deg, #fafafa, #e4772e 45%, #d8dde0 80%, #fafafa); }
  .contact {
    position: absolute; left: 0; top: 1036px; width: 848px;
    font-size: 20.5px; line-height: 28px;
  }
  .contact p { white-space: nowrap; }
  .contact .social { padding-left: 63px; }
  .contact .reach { padding-left: 91px; }
  .contact .place { padding-left: 125px; }
  .partners { position: absolute; top: 1132px; height: 60px; background: var(--white);
    display: flex; align-items: center; justify-content: center;
    font-family: "Catamaran", sans-serif; font-weight: 800; color: #222; font-size: 20px; }
  .partner-a { left: 200px; width: 176px; }
  .partner-b { left: 390px; width: 120px; }
  .partner-c { left: 522px; width: 78px; font-size: 15px; }
  .partner-d { left: 614px; width: 196px; }
</style>
</head>
<body>
<div class="flyer">
  <div class="backdrop" role="img" aria-label="Photo of a hire workshop with shelving, cutting saws and floor grinders"></div>
  <svg class="corner" viewBox="0 0 848 1200" aria-hidden="true">
    <polygon points="640,0 848,0 848,208" fill="var(--yellow)"/>
    <polygon points="0,1024 0,1200 256,1200" fill="var(--yellow)"/>
  </svg>

  <div class="logo-block">
    <span class="logo-mark"></span>
    <span class="logo-name">NORVALE RENTALS</span>
  </div>

  <h1 class="headline">NORVALE RENTALS<br>&amp; SUPPLY</h1>

  <h2 class="subhead">Concrete, construction and<br>communication hire equipment</h2>

  <ul class="services">
    <li>Honing, Polishing, Cutting, Drilling,Demolition and General Hire Equipment Available.</li>
    <li>Diamond Consumable for sale- core barrels, diamond segments and specialized tooling</li>
    <li>Good old fashion customer service with over 15 year's experience in the concrete and construction industry.</li>
  </ul>

  <div class="accent-bar"></div>
  <p class="promise">We will beat any written quote from our competitors.</p>

  <div class="product product-saw" role="img" aria-label="Photo of an orange ring cutting saw"></div>
  <div class="product product-grinder" role="img" aria-label="Photo of a red floor grinder with engine"></div>
  <div class="product product-vacuum" role="img" aria-label="Photo of an orange dust extractor vacuum"></div>

  <div class="contact">
    <p class="social">Find us on Linkbook and Snapgram</p>
    <p class="reach">Contact us: E: info@norvalerentals.com.au | W: www.norvalerentals.com.au</p>
    <p class="place">A: unit 1, 14 Harlow Ave Kendrick 6090 | P : 0491 570 156</p>
  </div>

  <div class="partners partner-a">KESTREL</div>
  <div class="partners partner-b">BRENMOR</div>
  <div class="partners partner-c">VOLTARO</div>
  <div class="partners partner-d">RIDGELINE</div>
</div>
</body>
</html>
```